Clockharbour Homepage Banner 1060 W x 100 H

Please see the attached 'word' document (Also copied below)
Feel free to use any images or logos from our website.
www.clockharbour.com.au

Background:
We are an Australian based official watch distributor/online retailer of international watch brands.

We require a new banner ad (1060 W x 100 H) to replace the existing one on our homepage www.clockharbour.com.au & wish to convey the following information:
*(Please feel free to alter wording, include or exclude points below & generally take creative license (with commercial reality in mind). We sell some luxury watches, so it must look professional & maintain a luxury look & feel.)

Clockharbour Direct:
Revolutionising the retail watch market !

- Buy direct from the official distributor & get world competitive
online prices (with full international warranty, & all original
papers, box & invoice)

- Eliminate all risk of fakes & non-existent factory warranty from
'grey' market sellers

- Free worldwide delivery over A$300

- Order online & 'try-on' in the comfort of your own home.
If you're not 100% happy, just post it back for a full refund or
exchange within 30 days

- Prefer to see & try on before purchase? Visit one of our retail
partner stores.

*** Feel free to copy any images from our website
www.clockharbour.com.au
Updates

Target Market(s)

Luxury watches

Industry/Entity Type

Retail

Font styles to use
Sans Serif

Requirements
Must have
• Visual imagery, text
Nice to have
• Feel free to use your creativity...
Should not have
• Cheap looking or tacky images. We sell some luxury watches, so we need to keep a professional & luxury image.

```html
<!DOCTYPE html>
<html lang="en">
<head>
<meta charset="utf-8">
<title>Clockharbour Direct – Homepage Banner</title>
<link rel="stylesheet" href="https://fonts.googleapis.com/css2?family=Cabin:wght@400;500&display=swap">
<style>
  :root {
    --page-bg: #f2f2f2;
    --navy-deep: #0a1330;
    --navy-mid: #132a63;
    --royal: #1d4fa3;
    --sky: #3aa3e0;
    --gold: #b8955a;
    --copy: #e9ecf4;
    --white: #ffffff;
    --dial-dark: #1c1f24;
    --steel: #b9bec6;
  }
  * { margin: 0; padding: 0; box-sizing: border-box; }
  html, body {
    width: 1200px;
    height: 256px;
    overflow: hidden;
    background: var(--page-bg);
    font-family: "Cabin", "Gill Sans", sans-serif;
  }
  .banner {
    position: absolute;
    left: 93px;
    top: 71px;
    width: 1045px;
    height: 99px;
    overflow: hidden;
    background: linear-gradient(90deg, var(--navy-deep) 0%, #0f1f4a 35%, var(--navy-mid) 60%, var(--royal) 80%);
  }
  .banner__shapes {
    position: absolute;
    inset: 0;
  }
  .banner__copy {
    position: absolute;
    left: 12px;
    top: 6px;
    color: var(--copy);
  }
  .banner__headline {
    font-weight: 400;
    font-size: 24px;
    letter-spacing: 0.3px;
    color: var(--gold);
    line-height: 28px;
    text-transform: uppercase;
  }
  .benefits {
    list-style: none;
    margin-top: 4px;
  }
  .benefits__item {
    display: flex;
    align-items: center;
    font-size: 11px;
    line-height: 14.5px;
  }
  .benefits__icon {
    width: 10px;
    height: 10px;
    margin-right: 6px;
    flex: none;
  }
  .product-photo {
    position: absolute;
    right: 0;
    top: 0;
    width: 234px;
    height: 99px;
    background: radial-gradient(circle at 48% 50%, var(--dial-dark) 0 34%, var(--sky) 36% 42%, var(--dial-dark) 44% 52%, var(--steel) 56% 64%, #eef0f3 72%);
  }
</style>
</head>
<body>
  <section class="banner" aria-label="Clockharbour Direct homepage banner">
    <svg class="banner__shapes" width="1045" height="99" viewBox="0 0 1045 99" aria-hidden="true">
      <polygon points="560,0 680,0 600,99 480,99" fill="#1a3d86" opacity="0.5"/>
      <polygon points="640,0 700,0 620,99 560,99" fill="#2456b0" opacity="0.45"/>
      <polygon points="740,0 790,0 760,40" fill="var(--sky)" opacity="0.8"/>
      <polygon points="755,0 1045,0 1045,99 691,99" fill="var(--white)"/>
    </svg>

    <div class="banner__copy">
      <h1 class="banner__headline">Revolutionising the retail watch market !</h1>
      <ul class="benefits">
        <li class="benefits__item">
          <svg class="benefits__icon" viewBox="0 0 10 10" aria-hidden="true"><circle cx="5" cy="5" r="4.3" fill="none" stroke="var(--gold)" stroke-width="1"/><path d="M4 3 L6 5 L4 7" fill="none" stroke="var(--gold)" stroke-width="1.1"/></svg>
          Buy direct from the official distributor &amp; get world competitive online prices
        </li>
        <li class="benefits__item">
          <svg class="benefits__icon" viewBox="0 0 10 10" aria-hidden="true"><circle cx="5" cy="5" r="4.3" fill="none" stroke="var(--gold)" stroke-width="1"/><path d="M4 3 L6 5 L4 7" fill="none" stroke="var(--gold)" stroke-width="1.1"/></svg>
          Eliminate all risk of fakes &amp; non-existent factory warranty from 'grey' market sellers
        </li>
        <li class="benefits__item">
          <svg class="benefits__icon" viewBox="0 0 10 10" aria-hidden="true"><circle cx="5" cy="5" r="4.3" fill="none" stroke="var(--gold)" stroke-width="1"/><path d="M4 3 L6 5 L4 7" fill="none" stroke="var(--gold)" stroke-width="1.1"/></svg>
          Free worldwide delivery over A$300
        </li>
        <li class="benefits__item">
          <svg class="benefits__icon" viewBox="0 0 10 10" aria-hidden="true"><circle cx="5" cy="5" r="4.3" fill="none" stroke="var(--gold)" stroke-width="1"/><path d="M4 3 L6 5 L4 7" fill="none" stroke="var(--gold)" stroke-width="1.1"/></svg>
          Order online &amp; 'try-on' in the comfort of your own home.
        </li>
      </ul>
    </div>

    <div class="product-photo" role="img" aria-label="Close-up photo of a steel chronograph watch with a black dial and bright blue bezel"></div>
  </section>
</body>
</html>
```